Face cream packaging | Cosmetic start-up

This project is about creating design proposals for two different types of packaging. Once to a cream jar made of glass and once to a jar made of plastic.
Three different designs must be created for each type of jar. Later, the different packaging will be used as customization options in an online store for cosmetics.

- The packaging variant made of glass should have color gradients. Three different shades are to be chosen. (Preferably with the primary colors red, blue and green). Note: The designer can create other proposals at will if he has better ideas. The logo must be included in some form. (Link to manufacturer description: https://catalogue.vorelpackwerk.com/en/portals/vorelpackwerk/assets/48302915/lio-50-ml/)

- With the plastic type of packaging, the designer has a lot of freedom to design. The only requirement is that the design must be artistic. It doesn't matter whether abstract patterns, geometric figures, mandalas or just a basic color is chosen. The main thing is that the packaging inspires. The logo must be included in some form. (Link to manufacturer description: https://catalogue.vorelpackwerk.com/en/portals/vorelpackwerk/assets/48302922/tova-50-ml/)

Thank you in advance for your work and best regards
Ubel

Target Market(s)

Young people with an affinity for social media and the web. Focus is on the female clientele.

Industry/Entity Type

Cosmetics

Font styles to use
Script

Colors
eea4c8
f59195
85cae6
cadf82

Requirements
Must have
• The logo must be included in some form. (PNG-File attached)
Nice to have
• Other types of packaging (can shape, packaging material)

```html
<!DOCTYPE html>
<html lang="en">
<head>
<meta charset="utf-8">
<title>Face Cream Label</title>
<link rel="stylesheet" href="https://fonts.googleapis.com/css2?family=Josefin+Sans:wght@300;400&display=swap">
<style>
  :root {
    --page: #ffffff;
    --ink: #1f5f86;
    --pattern-blue: #3a9bcf;
    --pattern-pale: #e8f3f9;
    --panel: #ffffff;
    --rule: #3a8fbf;
  }
  html, body {
    margin: 0;
    padding: 0;
    width: 1200px;
    height: 1200px;
    overflow: hidden;
    background: var(--page);
  }
  .canvas {
    position: relative;
    width: 1200px;
    height: 1200px;
    background: var(--page);
  }
  .label {
    position: absolute;
    left: 100px;
    top: 430px;
    width: 1000px;
    height: 340px;
    overflow: hidden;
  }
  .label-pattern {
    position: absolute;
    inset: 0;
  }
  .label-panel {
    position: absolute;
    left: 290px;
    top: 40px;
    width: 420px;
    height: 270px;
    background: var(--panel);
    display: flex;
    flex-direction: column;
    align-items: center;
    justify-content: center;
    font-family: "Josefin Sans", sans-serif;
    color: var(--ink);
  }
  .brand-name {
    font-weight: 300;
    font-size: 40px;
    line-height: 1.1;
    text-align: center;
    letter-spacing: 0.02em;
    margin: 0;
  }
  .brand-rule {
    width: 340px;
    height: 2px;
    background: var(--rule);
    margin: 18px 0 22px;
  }
  .product-name {
    font-weight: 300;
    font-size: 26px;
    letter-spacing: 0.32em;
    margin: 0 0 22px;
  }
  .product-volume {
    font-weight: 300;
    font-size: 28px;
    margin: 0;
  }
</style>
</head>
<body>
  <main class="canvas">
    <section class="label">
      <svg class="label-pattern" width="1000" height="340" viewBox="0 0 1000 340" role="img" aria-label="Blue mandala ornament pattern fading to white at the centre">
        <defs>
          <radialGradient id="pattern-fade" cx="50%" cy="50%" r="65%">
            <stop offset="0%" stop-color="var(--pattern-pale)"/>
            <stop offset="45%" stop-color="#cfe6f2"/>
            <stop offset="100%" stop-color="var(--pattern-blue)"/>
          </radialGradient>
        </defs>
        <rect width="1000" height="340" fill="url(#pattern-fade)"/>
      </svg>
      <div class="label-panel">
        <p class="brand-name">sola mae cosmetics</p>
        <div class="brand-rule"></div>
        <p class="product-name">FACE CREAM</p>
        <p class="product-volume">50ml</p>
      </div>
    </section>
  </main>
</body>
</html>
```